VELKORIS Stationery Design Project

I want a stationery design for a web development company consists of:
1- business card
2- Letter Head
3- small Envelope
4- Large Envelope

need a very clean professional simple design yet creative,

The company logo is attached
http://www.pixelbazaarhub.net/project-progress/designs.aspx?briefId=5830174&submissionId=47210938

logo font is sui generis rg (attached)
I would like to have the stationery text font to be helvetica font regular or light (can be changed)

I love the combination of cyan, black and grey colors
( will attach some recommended styles)

Business

• curves or waves

```html
<!DOCTYPE html>
<html lang="en">
<head>
<meta charset="utf-8">
<title>VELKORIS Stationery</title>
<link href="https://fonts.googleapis.com/css2?family=Open+Sans:wght@400;600&display=swap" rel="stylesheet">
<style>
  :root {
    --backdrop: #3a3a3a;
    --ink-black: #0d0d0d;
    --paper: #f3f3f3;
    --gold: #c9a84c;
    --brand-grey: #8c8c8c;
    --text-dark: #333333;
    --text-soft: #6b6b6b;
    --faint: #e2e2e2;
  }
  * { margin: 0; padding: 0; box-sizing: border-box; }
  html, body { width: 1200px; height: 680px; overflow: hidden; }
  body {
    background: var(--backdrop);
    font-family: "Open Sans", Helvetica, Arial, sans-serif;
    position: relative;
  }
  .piece { position: absolute; overflow: hidden; }

  .brand-name { letter-spacing: 0.14em; font-weight: 600; white-space: nowrap; }
  .brand-mark { display: inline-flex; align-items: center; gap: 0.5em; }
  .brand-square { display: inline-block; width: 0.9em; height: 0.9em; background: var(--gold); }

  /* Presentation folder */
  .folder { left: 80px; top: 82px; width: 304px; height: 406px; background: var(--ink-black); }
  .folder .brand-mark { position: absolute; left: 28px; top: 30px; font-size: 18px; color: var(--gold); }

  /* Letterhead */
  .letterhead { left: 448px; top: 84px; width: 305px; height: 405px; background: var(--paper); color: var(--text-dark); }
  .letterhead .brand-mark { position: absolute; left: 27px; top: 27px; font-size: 9px; color: var(--brand-grey); }
  .letter-address { position: absolute; left: 27px; top: 109px; font-size: 4.8px; line-height: 6.4px; }
  .letter-body { position: absolute; left: 27px; top: 143px; width: 252px; font-size: 4.8px; line-height: 6.9px; }
  .letter-closing { position: absolute; left: 27px; top: 262px; font-size: 4.8px; }
  .signature { position: absolute; left: 27px; top: 277px; width: 52px; height: 16px; background: linear-gradient(90deg, #d9d9d9, #cfcfcf); }
  .signer-title { position: absolute; left: 27px; top: 295px; font-size: 6px; font-style: italic; color: var(--text-soft); }
  .letter-footer { position: absolute; left: 27px; top: 376px; font-size: 3.9px; line-height: 8px; color: var(--text-soft); }
  .letter-footer .icon { display: inline-block; width: 4px; height: 4px; vertical-align: -0.5px; margin-right: 2px; }
  .faint-name { position: absolute; color: var(--faint); font-size: 11px; }
  .letterhead .faint-name { right: 20px; bottom: 22px; }

  /* Small envelope */
  .envelope-small { left: 808px; top: 146px; width: 320px; height: 152px; background: var(--paper); }
  .envelope-small .brand-mark { position: absolute; left: 23px; top: 16px; font-size: 8px; color: var(--brand-grey); }
  .envelope-small .faint-name { right: 22px; bottom: 16px; }

  /* Large envelope */
  .envelope-large { left: 808px; top: 335px; width: 320px; height: 153px; background: var(--paper); }
  .envelope-flap { position: absolute; left: 0; top: 0; }
  .envelope-large .brand-mark { position: absolute; left: 50%; top: 14px; transform: translateX(-50%); font-size: 8px; color: var(--gold); }
  .envelope-footer { position: absolute; left: 0; right: 0; bottom: 8px; text-align: center; font-size: 4px; color: var(--text-soft); letter-spacing: 0.08em; }
  .envelope-footer::before { content: ""; display: block; width: 150px; height: 0.5px; background: #bdbdbd; margin: 0 auto 3px; }

  /* Business cards */
  .card-back { left: 467px; top: 526px; width: 131px; height: 72px; background: var(--ink-black); }
  .card-back .brand-mark { position: absolute; left: 50%; top: 50%; transform: translate(-50%, -50%); font-size: 9px; color: var(--gold); }
  .card-front { left: 617px; top: 526px; width: 129px; height: 72px; background: var(--paper); color: var(--text-dark); }
  .card-front .brand-mark { position: absolute; left: 9px; top: 9px; font-size: 6.5px; color: var(--brand-grey); }
  .card-person { position: absolute; left: 9px; top: 42px; }
  .card-name { font-size: 4.6px; font-weight: 600; letter-spacing: 0.08em; }
  .card-role { font-size: 3.2px; color: var(--text-soft); }
  .card-contacts { position: absolute; left: 50px; top: 41px; font-size: 3.1px; line-height: 5px; color: var(--text-soft); }
  .card-address { position: absolute; left: 90px; top: 41px; font-size: 3.1px; line-height: 5px; color: var(--text-soft); }
</style>
</head>
<body>

  <div class="piece folder">
    <span class="brand-mark"><span class="brand-square"></span><span class="brand-name">VELKORIS</span></span>
  </div>

  <div class="piece letterhead">
    <span class="brand-mark"><span class="brand-square"></span><span class="brand-name">VELKORIS</span></span>
    <div class="letter-address">
      November 1, 2015<br>
      Mr. Tobin Marsh<br>
      58 Harlow Bend Road<br>
      Corvale, OR 40512
    </div>
    <div class="letter-body">
      <p>Dear Mr. Tobin</p>
      <p>The first paragraph of a typical business letter is used to state the main point of the letter. Begin with a friendly opening, then quickly transition into the purpose of your letter. Use a couple of sentences to explain the purpose, but do not go in to detail until the next paragraph.</p>
      <p>Beginning with the second paragraph, state the supporting details to justify your purpose. These may take the form of background information, statistics or first-hand accounts.</p>
      <p>A few short paragraphs within the body of the letter should be enough to support your reasoning. These may take the form of background information, statistics or first-hand accounts.</p>
      <p>A few short paragraphs within the body of the letter should be enough to support your reasoning. These may take the form of background information, statistics or first-hand accounts. A few short paragraphs within the body of the letter should be enough to support your reasoning.</p>
      <p>Finally, in the closing paragraph, briefly restate your purpose and why it is important. If the purpose of your letter is related to your employment, consider ending your letter with your contact information and title if it is not included on letterhead. However, if the purpose is informational, think about closing with gratitude for the reader's time.</p>
    </div>
    <div class="letter-closing">Sincerely,</div>
    <div class="signature" role="img" aria-label="Handwritten signature"></div>
    <div class="signer-title">President</div>
    <div class="letter-footer">
      <svg class="icon" viewBox="0 0 10 10"><path d="M2 1h2l1 3-1.5 1a6 6 0 0 0 2.5 2.5L7 6l3 1v2c-5 0-9-4-9-8z" fill="#777"/></svg>415.280.6634 &nbsp;|&nbsp; info@velkoris.com &nbsp;|&nbsp; www.velkoris.com<br>
      <svg class="icon" viewBox="0 0 10 10"><path d="M5 0a3.5 3.5 0 0 0-3.5 3.5C1.5 6 5 10 5 10s3.5-4 3.5-6.5A3.5 3.5 0 0 0 5 0z" fill="#777"/></svg>27 Kestrel Row, Dunmore Hills, WA 98231
    </div>
    <span class="faint-name brand-name">VELKORIS</span>
  </div>

  <div class="piece envelope-small">
    <span class="brand-mark"><span class="brand-square"></span><span class="brand-name">VELKORIS</span></span>
    <span class="faint-name brand-name">VELKORIS</span>
  </div>

  <div class="piece envelope-large">
    <svg class="envelope-flap" width="320" height="60" viewBox="0 0 320 60">
      <path d="M0 0H320V8Q314 40 290 44H30Q6 40 0 8Z" fill="var(--ink-black)"/>
    </svg>
    <span class="brand-mark"><span class="brand-square"></span><span class="brand-name">VELKORIS</span></span>
    <div class="envelope-footer">415.280.6634 &nbsp;|&nbsp; WWW.VELKORIS.COM</div>
  </div>

  <div class="piece card-back">
    <span class="brand-mark"><span class="brand-square"></span><span class="brand-name">VELKORIS</span></span>
  </div>

  <div class="piece card-front">
    <span class="brand-mark"><span class="brand-square"></span><span class="brand-name">VELKORIS</span></span>
    <div class="card-person">
      <div class="card-name">ADRIAN VOSS</div>
      <div class="card-role">DIRECTOR</div>
    </div>
    <div class="card-contacts">
      +1 415 280 6634<br>
      info@velkoris.com<br>
      www.velkoris.com
    </div>
    <div class="card-address">
      27 Kestrel Row<br>
      Dunmore Hills, WA
    </div>
  </div>

</body>
</html>
```